Vitalquorra.com

I need a web design for a Online Wellness Center based in Chicago, IL and it's called "Vitalquorra" We provide Health risk assessment to individuals and interventions. Our portal has a Health Activity tracker where our members record health activities and aerobic miles and biometric data. Our Online wellness center tracks the participant's progress toward health goals and awards points for completed activities.
I started working on this website but the designer was not able to designer a website which describes what we do. I need a fresh look on this project. I need a very attractive, responsive website which says what we do.
These are the things we do.
1. We provide Health Risk Assessments to individuals and Co-operations
2. We Provide Free health screenings to undeserved communities
3. Assist individuals access free or affordable medications
4. We ask providers/doctors to see (or do a complete physical) one individual free of charge once a year (those individuals who are no insured and don't have money to pay from their pocket)
5. Assist patient access lab work at low cost
Our goal is to provide services that will lower the cost of care for our members.

Here is the website: www.vitalquorra.com still underdevelopment. PLEASE DO NOT COPY THIS STYLE OF WEBSITE. IT'S A BAD DESIGN AND THAT IS WHY I'M RE-DESIGNING THE SITE

Target Market(s)

Health individuals between the age of 21 to 65 Plus years old. Insured and uninsured

Industry/Entity Type

Health And Wellness

Coding

Coded - Design and coding required

Number of Pages Required

5+ page

Colors
0292cd

Requirements
Must have
• I'm still working on this websiteHere is the menu: Home, About us, Services, Health Screening, Providers, Contacts
• Please see. www.vitalquorra.com
Nice to have
• Event calender
• Upcoming Event
• Medication
• Lab assist
• Providers/Free Clinics

```html
<!DOCTYPE html>
<html lang="en">
<head>
<meta charset="utf-8">
<title>Vitalquorra – Online Wellness Center</title>
<link href="https://fonts.googleapis.com/css2?family=Open+Sans:wght@400;600;700;800&display=swap" rel="stylesheet">
<style>
:root{
  --blue:#0292cd;
  --blue-dark:#0278ad;
  --blue-light:#35b0e3;
  --green:#7cc242;
  --green-dark:#5ea52a;
  --ink:#3a3a3a;
  --muted:#7a7a7a;
  --line:#e3e3e3;
  --paper:#ffffff;
  --soft:#f4f6f7;
}
*{box-sizing:border-box;margin:0;padding:0}
html,body{width:1200px;height:2772px;overflow:hidden}
body{font-family:"Open Sans",Arial,sans-serif;color:var(--ink);background:var(--paper);position:relative}
.btn{display:inline-block;background:var(--green);color:#fff;font-size:13px;font-weight:600;padding:9px 20px;border-radius:2px}

/* header */
.site-header{position:absolute;top:0;left:0;width:1200px;height:72px;background:#fff;display:flex;align-items:center;padding:0 60px;border-bottom:1px solid var(--line)}
.brand{display:flex;align-items:center;gap:8px;font-size:28px;font-weight:700;color:var(--blue);width:310px}
.brand-dot{width:22px;height:22px;border-radius:50%;background:var(--green)}
.main-nav{display:flex;gap:4px}
.main-nav a{font-size:12px;font-weight:600;color:var(--ink);padding:10px 13px;text-decoration:none;text-transform:uppercase;white-space:nowrap}
.main-nav a.active{background:var(--blue);color:#fff}
.search{margin-left:auto;width:170px;height:30px;border:1px solid var(--line);border-radius:2px;display:flex;align-items:center;justify-content:flex-end;padding-right:8px}

/* hero */
.hero{position:absolute;top:72px;left:0;width:1200px;height:488px;background:linear-gradient(180deg,var(--blue-light),var(--blue))}
.hero-photo{position:absolute;left:120px;top:0;width:500px;height:488px;background:linear-gradient(180deg,#cfe8f4,#9fd0ea)}
.hero-copy{position:absolute;left:690px;top:120px;width:420px;color:#fff}
.hero-copy h1{font-size:36px;line-height:1.15;font-weight:800;text-transform:uppercase}
.hero-copy p{font-size:14px;line-height:1.5;margin:14px 0 22px}
.dots{position:absolute;bottom:18px;left:0;width:100%;display:flex;justify-content:center;gap:10px}
.dots span{width:10px;height:10px;border-radius:50%;background:rgba(255,255,255,.55)}
.dots span.on{background:var(--green)}

/* panel sections */
.band{position:absolute;left:0;width:1200px;padding:22px 24px}
.band.green{background:var(--green)}
.band.blue{background:var(--blue)}
.panel{background:#fff;height:100%;padding:40px 60px;overflow:hidden}
h2.section-title{font-size:30px;font-weight:700;color:var(--blue);text-transform:uppercase;margin-bottom:14px;white-space:nowrap}
.lead{font-size:13px;line-height:1.6;color:var(--blue)}

.services{top:560px;height:590px}
.service-grid{display:grid;grid-template-columns:repeat(4,1fr);gap:40px;margin-top:34px;text-align:center}
.service-icon{width:150px;height:150px;border-radius:50%;background:var(--blue);margin:0 auto 18px;display:flex;align-items:center;justify-content:center}
.service h3{font-size:22px;font-weight:700;color:var(--blue);margin-bottom:6px}
.service p{font-size:12px;line-height:1.5;color:var(--muted);margin-bottom:14px}
.service .btn{background:var(--blue)}

.benefits{top:1150px;height:420px}
.benefits .panel{display:flex;gap:30px;padding:30px 60px}
.benefits-copy{width:650px}
.benefits-copy h2.section-title{font-size:28px;margin-bottom:10px}
.benefits-copy ul{list-style:none;font-size:13px;line-height:1.6;margin:12px 0 16px}
.benefits-copy ul li::before{content:"• ";color:var(--blue)}
.benefits-photo{flex:1;background:linear-gradient(135deg,#f2f2f2,#c9ced2);border-radius:4px}

/* events */
.events{position:absolute;top:1570px;left:0;width:1200px;height:420px;background:var(--soft);padding:40px 84px}
.event-grid{display:grid;grid-template-columns:1fr 1fr;gap:40px;margin-top:16px}
.event{display:flex;gap:20px;background:#fff;padding:16px;border:1px solid var(--line)}
.event-photo{width:200px;height:150px;flex:none;background:linear-gradient(135deg,#b9d7e6,#6f98ad)}
.event h3{font-size:18px;font-weight:700;color:var(--blue);margin-bottom:6px}
.event p{font-size:12px;line-height:1.5;color:var(--muted);margin-bottom:12px}
.view-all{text-align:center;margin-top:26px}
.view-all .btn{background:var(--blue)}

/* schedule */
.schedule{position:absolute;top:1990px;left:0;width:1200px;height:520px;background:var(--blue);padding:40px 84px;color:#fff}
.schedule-head{display:flex;justify-content:space-between;align-items:center}
.schedule-head h2{font-size:28px;font-weight:700;text-transform:uppercase}
.schedule-body{display:flex;gap:40px;margin-top:30px}
.views{width:240px;padding-left:80px;padding-top:120px;display:flex;flex-direction:column;gap:10px}
.views span{background:#fff;color:var(--blue);font-size:12px;padding:7px 14px;width:110px}
.calendar{width:560px;background:#fff;color:var(--ink);padding:16px 24px}
.cal-head{display:flex;justify-content:space-between;align-items:center;color:var(--blue);font-size:20px;font-weight:600;padding-bottom:10px;border-bottom:1px solid var(--line)}
.cal-grid{display:grid;grid-template-columns:repeat(7,1fr);text-align:center;font-size:14px;row-gap:16px;margin-top:14px}
.cal-grid .dow{font-weight:700;color:var(--blue)}
.cal-grid .out{color:#c2c2c2}
.cal-grid .today span{display:inline-block;width:28px;height:28px;line-height:26px;border:2px solid var(--blue);border-radius:50%}

/* footer */
.site-footer{position:absolute;top:2510px;left:0;width:1200px;height:230px;background:#fff;padding:30px 150px;display:grid;grid-template-columns:1fr 1.3fr 1.3fr 1.3fr;gap:30px;font-size:11px;color:var(--muted)}
.site-footer h4{font-size:12px;font-weight:700;color:var(--blue);text-transform:uppercase;margin-bottom:10px}
.site-footer li{list-style:none;line-height:1.9;text-transform:uppercase}
.site-footer p{line-height:1.6}
.socials{display:flex;gap:8px;margin-bottom:14px}
.socials span{width:24px;height:24px;border-radius:50%;background:var(--blue)}
.news{display:flex;margin-top:6px}
.news span:first-child{flex:1;border:1px solid var(--line);height:24px;padding:4px 6px}
.news span:last-child{background:var(--green);color:#fff;padding:4px 10px}
.tweet{border-bottom:1px solid var(--line);padding:6px 0}
.tweet b{color:var(--blue)}
.bottom-bar{position:absolute;top:2740px;left:0;width:1200px;height:32px;background:var(--green);color:#fff;font-size:11px;display:flex;align-items:center;justify-content:center}
</style>
</head>
<body>

<header class="site-header">
  <div class="brand"><span class="brand-dot"></span>Vitalquorra</div>
  <nav class="main-nav">
    <a class="active">Home</a><a>About</a><a>Services</a><a>Health Screening</a><a>Providers</a><a>Contact</a>
  </nav>
  <div class="search">
    <svg width="14" height="14" viewBox="0 0 14 14"><circle cx="6" cy="6" r="4.5" fill="none" stroke="#999" stroke-width="1.5"/><line x1="9.5" y1="9.5" x2="13" y2="13" stroke="#999" stroke-width="1.5"/></svg>
  </div>
</header>

<section class="hero">
  <div class="hero-photo" role="img" aria-label="Smiling doctor in a white coat with a stethoscope, gesturing to the headline"></div>
  <div class="hero-copy">
    <h1>Professional and accurate screening reports!</h1>
    <p>Lorem ipsum dolor sit amet, consectetur adipiscing elit, sed do eiusmod tempor incididunt ut labore et dolore magna aliqua.</p>
    <span class="btn">Read more</span>
  </div>
  <div class="dots"><span></span><span class="on"></span><span></span></div>
</section>

<section class="band green services">
  <div class="panel">
    <h2 class="section-title">Our Wellness Services</h2>
    <p class="lead">Vitalquorra is an online wellness center whose objective is to make it possible to reach quality health at a fair price. Our wellness services provide free medication, free health screening, lab testing and wellness products, and we ask providers and free clinics to see one uninsured individual each year at no charge to lower their cost of care.</p>
    <div class="service-grid">
      <div class="service">
        <div class="service-icon">
          <svg width="80" height="80" viewBox="0 0 80 80"><g transform="rotate(-40 40 40)"><rect x="12" y="28" width="56" height="24" rx="12" fill="#fff"/><rect x="40" y="28" width="28" height="24" rx="0" fill="#cfeaf7"/><rect x="52" y="28" width="16" height="24" rx="12" fill="#cfeaf7"/></g></svg>
        </div>
        <h3>Medication</h3>
        <p>One of our most focused services helps members find free or affordable medication near them.</p>
        <span class="btn">Read more</span>
      </div>
      <div class="service">
        <div class="service-icon">
          <svg width="80" height="80" viewBox="0 0 80 80"><path d="M40 68 L12 40 A15 15 0 0 1 40 20 A15 15 0 0 1 68 40 Z" fill="#fff"/><path d="M28 42 L37 51 L54 33" fill="none" stroke="#0292cd" stroke-width="6" stroke-linecap="round" stroke-linejoin="round"/></svg>
        </div>
        <h3>Health Screening</h3>
        <p>Our free health screening events bring checkups to underserved communities across the city.</p>
        <span class="btn">Read more</span>
      </div>
      <div class="service">
        <div class="service-icon">
          <svg width="80" height="80" viewBox="0 0 80 80"><path d="M32 12 H48 M35 12 V34 L18 64 A4 4 0 0 0 22 70 H58 A4 4 0 0 0 62 64 L45 34 V12" fill="none" stroke="#fff" stroke-width="5" stroke-linejoin="round"/><path d="M25 56 H55 L60 66 H20 Z" fill="#fff"/></svg>
        </div>
        <h3>Lab Test</h3>
        <p>Lab testing service helps you get the lab work you need at low cost with trusted partners.</p>
        <span class="btn">Read more</span>
      </div>
      <div class="service">
        <div class="service-icon">
          <svg width="80" height="80" viewBox="0 0 80 80"><path d="M28 28 V22 A12 12 0 0 1 52 22 V28" fill="none" stroke="#fff" stroke-width="5"/><rect x="16" y="28" width="48" height="40" rx="4" fill="#fff"/><path d="M40 38 V58 M30 48 H50" stroke="#0292cd" stroke-width="6"/></svg>
        </div>
        <h3>Wellness products</h3>
        <p>We help members choose wellness products that support their goals and earn activity points.</p>
        <span class="btn">Read more</span>
      </div>
    </div>
  </div>
</section>

<section class="band blue benefits">
  <div class="panel">
    <div class="benefits-copy">
      <h2 class="section-title">Benefits of our wellness services</h2>
      <p class="lead">Our community is serving precisely to share the health wellness services and choose the suitable plans for you. View the features:</p>
      <ul>
        <li>Free wellness articles</li>
        <li>Health tips</li>
        <li>Free health assessment report</li>
        <li>Affordable screening</li>
        <li>Accurate report card</li>
        <li>Health screening camps</li>
        <li>Saves your time, money and keeps your health record</li>
      </ul>
      <span class="btn">Read more</span>
    </div>
    <div class="benefits-photo" role="img" aria-label="Stethoscope lying on a white surface"></div>
  </div>
</section>

<section class="events">
  <h2 class="section-title">Upcoming Health Screening Events</h2>
  <div class="event-grid">
    <article class="event">
      <div class="event-photo" role="img" aria-label="Nurse measuring a patient's blood pressure"></div>
      <div>
        <h3>Health Campus</h3>
        <p>Vitalquorra is going to organise a event for the poor patient to check up their body problems and fix them instantly for the people who are feeble in their life and can't visit us.</p>
        <span class="btn">Read more</span>
      </div>
    </article>
    <article class="event">
      <div class="event-photo" role="img" aria-label="Pharmacist handing medication to a customer"></div>
      <div>
        <h3>Medication Event</h3>
        <p>The mission of Vitalquorra is to reach people and cure their disease and provide a healthy life and make a healthy and disease free world.</p>
        <span class="btn">Read more</span>
      </div>
    </article>
  </div>
  <div class="view-all"><span class="btn">View All</span></div>
</section>

<section class="schedule">
  <div class="schedule-head">
    <h2>Our Screening Schedule</h2>
    <span class="btn">Create event</span>
  </div>
  <div class="schedule-body">
    <div class="views"><span>Today</span><span>Month</span><span>Week</span></div>
    <div class="calendar">
      <div class="cal-head"><span>‹</span><span>August</span><span>›</span></div>
      <div class="cal-grid">
        <div class="dow">S</div><div class="dow">M</div><div class="dow">T</div><div class="dow">W</div><div class="dow">T</div><div class="dow">F</div><div class="dow">S</div>
        <div class="out">30</div><div class="out">31</div><div>1</div><div>2</div><div class="today"><span>3</span></div><div>4</div><div>5</div>
        <div>6</div><div>7</div><div>8</div><div>9</div><div>10</div><div>11</div><div>12</div>
        <div>13</div><div>14</div><div>15</div><div>16</div><div>17</div><div>18</div><div>19</div>
        <div>20</div><div>21</div><div>22</div><div>23</div><div>24</div><div>25</div><div>26</div>
        <div>27</div><div>28</div><div>29</div><div>30</div><div>31</div><div class="out">1</div><div class="out">2</div>
      </div>
    </div>
  </div>
</section>

<footer class="site-footer">
  <div>
    <ul><li>Home</li><li>About</li><li>Services</li><li>Health Screening</li><li>Providers</li><li>Contact</li></ul>
  </div>
  <div>
    <h4>Contact</h4>
    <p>Vitalquorra<br>418 Larkspur Avenue<br>Chicago, IL 60614</p>
    <p style="margin-top:8px">Phone: (312) 555-0147<br>info@vitalquorra.com<br>www.vitalquorra.com</p>
  </div>
  <div>
    <h4>Follow us</h4>
    <div class="socials"><span></span><span></span><span></span><span></span></div>
    <h4>Join our newsletter</h4>
    <div class="news"><span>your email</span><span>Go</span></div>
  </div>
  <div>
    <h4>Recent tweets</h4>
    <div class="tweet"><b>Vitalquorra</b> @vitalquorra<br>Free screening this Saturday, join us</div>
    <div class="tweet"><b>Vitalquorra</b> @vitalquorra<br>New lab partners added this month</div>
    <div class="tweet"><b>Vitalquorra</b> @vitalquorra<br>Track your aerobic miles and earn points</div>
  </div>
</footer>
<div class="bottom-bar">© Vitalquorra. All rights reserved.</div>

</body>
</html>
```